Curbside Bin Butler Valet Trash Recycling

I want to create a colorful brochure, I really like my company colors, with basic information about valet trash for apartment complexes. You can include some apartment recycling information as well, but 80% trash, 20% recycling. I have included my logo in the attachments. Also, you can find information at curbsidebinbutler.example, very basic and I will be redoing my website as well.

many people are giving information about business and residential recycling, I only want information on trash and recycling valet for apartments

Target Market(s)

apartment complex tenants and management

Industry/Entity Type

Apartment

Number of Pages Required

4 page

Font styles to use
Serif
Sans Serif

Colors
9bcb3b
f37122
0355a3

Requirements
Must have
• Tri-Fold brochure, colorful, well organized. Advantages for tenants and for property management.

```html
<!DOCTYPE html>
<html lang="en">
<head>
<meta charset="utf-8">
<title>Curbside Bin Butler – Tri-Fold Brochure</title>
<link href="https://fonts.googleapis.com/css2?family=Roboto+Slab:wght@400;700&family=Roboto+Condensed:ital,wght@0,400;0,700;1,700&family=Open+Sans:wght@400;700&display=swap" rel="stylesheet">
<style>
:root{
  --green:#8cc63f;
  --green-dark:#5fae3a;
  --orange:#f37122;
  --blue:#0355a3;
  --navy:#1d3a8f;
  --navy-deep:#172f78;
  --sky:#dfe7ef;
  --ink:#1b1b1b;
  --paper:#ffffff;
  --stage:#d9dadc;
}
*{box-sizing:border-box;margin:0;padding:0}
html,body{width:1200px;height:998px;overflow:hidden;background:var(--stage)}
.brochure{position:absolute;left:30px;top:29px;width:1140px;height:940px;display:flex;box-shadow:0 6px 24px rgba(0,0,0,.18)}
.panel{position:relative;width:380px;height:940px;overflow:hidden}
.panel svg.wave{position:absolute;left:0;width:380px}

/* left panel */
.panel--about{background:var(--paper);color:var(--ink);font-family:"Roboto Condensed",sans-serif}
.pill{display:block;margin:34px auto 18px;width:300px;padding:8px 0;border-radius:22px;background:linear-gradient(180deg,#2f52b8,var(--navy-deep));color:#fff;text-align:center;font-family:"Roboto Slab",serif;font-weight:700;font-style:italic;font-size:19px;letter-spacing:.5px;box-shadow:0 3px 0 rgba(0,0,0,.15)}
.about-copy{padding:0 42px;text-align:center;font-size:14px;line-height:1.35}
.about-copy p{margin-bottom:14px}
.pill--services{margin-top:22px}
.tagline{margin:10px 0 16px;color:var(--blue);font-weight:700;font-style:italic;font-size:17px;line-height:1.2}
.contact-mini{font-size:14px;line-height:1.75}
.panel--about .wave{bottom:0;height:260px}

/* middle panel */
.panel--contact{background:linear-gradient(180deg,#22409a 0%,var(--navy) 50%,#173178 100%);color:#fff;font-family:"Roboto Slab",serif}
.brand{display:flex;align-items:center;gap:10px;justify-content:center}
.brand-dot{width:16px;height:16px;border-radius:50%;background:var(--orange)}
.brand-name{font-family:"Open Sans",sans-serif;font-weight:400;font-size:24px;color:#fff}
.panel--contact .brand{margin-top:82px}
.brand-url{text-align:center;color:var(--orange);font-family:"Open Sans",sans-serif;font-size:12px;margin-top:2px;padding-left:70px}
.person{margin:46px 0 0 70px}
.person h2{color:var(--green);font-size:30px;font-weight:700;margin-bottom:8px}
.person .line{display:flex;align-items:flex-start;gap:8px;font-size:17px;line-height:1.3}
.person .line svg{flex:none;margin-top:4px}
.person .indent{padding-left:22px}
.web-lines{margin:10px 0 0 30px}
.web-lines .line{display:flex;gap:8px;align-items:center;font-size:17px;line-height:1.55}
.partner{margin:46px 0 0;text-align:center;font-weight:700;font-size:20px}
.badge{width:280px;height:200px;margin:14px auto 0;background:#fff;border-radius:16px;border:4px solid #dfe6f2}
.panel--contact .brand--footer{position:absolute;left:0;right:0;bottom:120px}
.brand--footer .brand-name{font-size:28px}

/* cover panel */
.panel--cover{background:var(--navy)}
.cover-head{position:absolute;left:0;top:0;width:380px;height:232px;background:var(--sky)}
.cover-head .brand{margin-top:50px}
.cover-head .brand-name{color:var(--blue);font-size:27px}
.cover-head .brand-url{padding-left:150px}
.headline{margin:26px 0 0 30px;font-family:"Open Sans",sans-serif;font-weight:700;line-height:1.1}
.headline .top{color:var(--orange);font-size:25px}
.headline .bottom{color:var(--navy-deep);font-size:21px}
.photo{position:absolute;left:0;top:232px;width:380px;height:400px;background:linear-gradient(160deg,#b9c3cc 0%,#8c7d6e 45%,#6e6558 100%)}
.panel--cover .wave{top:420px;height:260px}
.cover-copy{position:absolute;left:0;top:682px;width:380px;padding:0 30px;color:#fff;font-family:"Roboto Slab",serif;text-align:center}
.city{color:var(--green);font-family:"Open Sans",sans-serif;font-size:30px;font-weight:400;margin-bottom:14px}
.cover-copy p{font-size:15px;line-height:1.35}
.cover-copy .promise{font-weight:700;margin-top:2px}
.cover-copy .url{color:var(--green);font-weight:700;font-size:19px;margin-top:26px}
</style>
</head>
<body>
<main class="brochure">

  <section class="panel panel--about">
    <h2 class="pill">ABOUT THE COMPANY</h2>
    <div class="about-copy">
      <p>Curbside Bin Butler (CBB) is a Houston-based business created by Marcus Delvane, a Bayou City College student and professional mixed martial artist. Marcus previously owned and operated the successful trash removal service, Marcus's Haul-Away, while he was a high school student-athlete in Galveston. He has now founded a similar service in the Houston area.</p>
      <p>Marcus plans to keep CBB ahead of its competitors by focusing on customer satisfaction, technology, efficiency, and professionalism.</p>
      <p>CBB is fully ensured; proof of insurance will be provided upon request.</p>
      <p>Testimonials from former clients reveal so much about how a company operates and performs. We are happy to provide references upon request.</p>
    </div>
    <h2 class="pill pill--services">CBB SERVICES</h2>
    <div class="about-copy">
      <p>Curbside Bin Butler (CBB) is a complete trash and recycling valet service designed to keep apartment complexes and its units clean, make complexes more environmentally friendly, and to keep tenants satisfied.</p>
      <p class="tagline">Keeping Apartment Complexes Cleaner and Greener Across Houston.</p>
      <div class="contact-mini">
        <div>curbsidebinbutler.example</div>
        <div>hello@curbsidebinbutler.example</div>
        <div>409-555-0182</div>
      </div>
    </div>
    <svg class="wave" viewBox="0 0 380 260" preserveAspectRatio="none" aria-hidden="true">
      <path d="M0 20 C30 150 140 230 380 230 L380 260 L0 260Z" fill="var(--green)"/>
      <path d="M0 70 C40 170 150 235 380 238 L380 260 L0 260Z" fill="var(--green-dark)"/>
      <path d="M0 190 C60 225 130 240 200 248 L0 260Z" fill="var(--blue)"/>
      <path d="M60 200 C150 250 280 250 380 205 L380 222 C280 262 160 262 60 200Z" fill="var(--orange)"/>
      <path d="M0 215 C60 245 150 255 380 246 L380 260 L0 260Z" fill="#fff"/>
    </svg>
  </section>

  <section class="panel panel--contact">
    <div class="brand"><span class="brand-dot"></span><span class="brand-name">Curbside Bin Butler</span></div>
    <div class="brand-url">curbsidebinbutler.example</div>
    <div class="person">
      <h2>Marcus Delvane</h2>
      <div class="line">
        <svg width="12" height="16" viewBox="0 0 12 16" aria-hidden="true"><path d="M6 0a6 6 0 0 0-6 6c0 4.5 6 10 6 10s6-5.5 6-10a6 6 0 0 0-6-6zm0 8.5A2.5 2.5 0 1 1 6 3.5a2.5 2.5 0 0 1 0 5z" fill="#fff"/></svg>
        <span>4720 Harlow Lane #118<br>Bellaire, TX 77401</span>
      </div>
      <div class="line">
        <svg width="14" height="14" viewBox="0 0 14 14" aria-hidden="true"><path d="M3 1l2 3-1.3 1.3a8 8 0 0 0 5 5L10 9l3 2-1 2.5C6 13 1 8 .5 2z" fill="#fff"/></svg>
        <span>409-555-0182</span>
      </div>
    </div>
    <div class="web-lines">
      <div class="line"><svg width="15" height="11" viewBox="0 0 15 11" aria-hidden="true"><rect x=".5" y=".5" width="14" height="10" fill="none" stroke="#fff"/><path d="M.5.5l7 5 7-5" fill="none" stroke="#fff"/></svg><span>hello@curbsidebinbutler.example</span></div>
      <div class="line"><svg width="14" height="14" viewBox="0 0 14 14" aria-hidden="true"><circle cx="7" cy="7" r="6.3" fill="none" stroke="#fff"/><ellipse cx="7" cy="7" rx="2.8" ry="6.3" fill="none" stroke="#fff"/><path d="M.7 7h12.6" stroke="#fff"/></svg><span>curbsidebinbutler.example</span></div>
    </div>
    <p class="partner">CBB is partnered with</p>
    <div class="badge" role="img" aria-label="Partner badge"></div>
    <div class="brand brand--footer"><span class="brand-name">Curbside Bin Butler</span></div>
  </section>

  <section class="panel panel--cover">
    <header class="cover-head">
      <div class="brand"><span class="brand-dot"></span><span class="brand-name">Curbside Bin Butler</span></div>
      <div class="brand-url">curbsidebinbutler.example</div>
      <h1 class="headline"><span class="top">FULL-SERVICE WASTE</span><br><span class="bottom">REMOVAL AND RECYCLING</span></h1>
    </header>
    <div class="photo" role="img" aria-label="Photo of a smiling valet carrying a full trash bag over his shoulder past a wooden fence"></div>
    <svg class="wave" viewBox="0 0 380 260" preserveAspectRatio="none" aria-hidden="true">
      <path d="M0 0 C10 110 90 190 380 200 L380 260 L0 260Z" fill="var(--green)"/>
      <path d="M0 150 C90 200 220 215 380 212 L380 260 L0 260Z" fill="#fff"/>
      <path d="M0 170 C100 215 230 228 380 226 L380 260 L0 260Z" fill="var(--navy)"/>
      <path d="M90 190 C190 235 300 240 380 222 L380 248 C290 262 180 250 90 190Z" fill="var(--orange)"/>
    </svg>
    <div class="cover-copy">
      <h2 class="city">HOUSTON, TEXAS</h2>
      <p>Taking out somebody's trash is a timeless gesture of kindness. Curbside Bin Butler (CBB) takes that act of kindness one step further:</p>
      <p class="promise">your tenants will never again have to bother with trash past their own doorsteps!</p>
      <p class="url">www.curbsidebinbutler.example</p>
    </div>
  </section>

</main>
</body>
</html>
```